Uprising SaaS company needs an attractive business card design

We're an uprising SaaS company who's attempting to attack the rigid car (insurance) claims management market in Europe.
We want to our mighty base order management system, listen to our clients to connect the smart ideas to build something even mightier.
We primarily focus on helping our customers manage their customers' claims/orders and get them resolved as smoothly as possible.
We'd like the business card design to express technical innovation and the fact that we connect smart ideas, as our company slogan indicates.
Contact Information for Business Card
Name, position, website, email, mobile, business address
Font styles to use
Colors
Designer to choose colors to be used in the design.
Look and feel
Each slider illustrates characteristics of the customer's brand and the style your logo design should communicate.

```html
<!DOCTYPE html>
<html lang="en">
<head>
<meta charset="utf-8">
<title>Corvanta – Business Card</title>
<link rel="stylesheet" href="https://fonts.googleapis.com/css2?family=Montserrat:wght@300;400;800&display=swap">
<style>
  :root {
    --card-bg: #2b2b2e;
    --text-white: #ffffff;
    --brand-cyan: #5ec4dc;
    --tagline-grey: #a9b4b8;
    --icon-cyan: #5ec4dc;
  }
  html, body {
    margin: 0;
    padding: 0;
    width: 1200px;
    height: 777px;
    overflow: hidden;
    background: var(--card-bg);
  }
  .card {
    position: relative;
    width: 1200px;
    height: 777px;
    background: var(--card-bg);
    font-family: "Montserrat", sans-serif;
    color: var(--text-white);
    overflow: hidden;
  }
  .brand {
    position: absolute;
    right: 72px;
    top: 118px;
    text-align: right;
  }
  .brand-name {
    display: flex;
    align-items: center;
    justify-content: flex-end;
    gap: 22px;
    margin: 0;
    font-weight: 400;
    font-size: 92px;
    line-height: 1;
    color: var(--brand-cyan);
  }
  .brand-dot {
    width: 26px;
    height: 26px;
    border-radius: 50%;
    background: var(--brand-cyan);
    flex: none;
  }
  .brand-tagline {
    margin: 22px 0 0;
    font-weight: 300;
    font-size: 38px;
    letter-spacing: 1px;
    color: var(--tagline-grey);
  }
  .person {
    position: absolute;
    left: 72px;
    top: 380px;
  }
  .person-name {
    margin: 0;
    font-weight: 800;
    font-size: 60px;
    line-height: 1;
    letter-spacing: 1px;
  }
  .person-role {
    margin: 14px 0 0;
    font-weight: 300;
    font-size: 50px;
    line-height: 1;
  }
  .contacts {
    position: absolute;
    left: 76px;
    top: 566px;
    margin: 0;
    padding: 0;
    list-style: none;
  }
  .contact-item {
    display: flex;
    align-items: center;
    height: 52px;
    font-weight: 400;
    font-size: 33px;
  }
  .contact-icon {
    width: 40px;
    height: 40px;
    margin-right: 16px;
    flex: none;
  }
</style>
</head>
<body>
  <main class="card">
    <header class="brand">
      <h1 class="brand-name"><span class="brand-dot"></span>Corvanta</h1>
      <p class="brand-tagline">claims made simple</p>
    </header>

    <section class="person">
      <h2 class="person-name">Lukas Brenner</h2>
      <p class="person-role">CEO</p>
    </section>

    <ul class="contacts">
      <li class="contact-item">
        <svg class="contact-icon" viewBox="0 0 40 40" aria-hidden="true">
          <circle cx="20" cy="20" r="18" fill="var(--icon-cyan)"/>
          <path d="M14 11c1-1 2.5-1 3 0l2 4c.4.8 0 1.6-.6 2l-1.4 1c1 2.4 2.6 4 5 5l1-1.4c.5-.6 1.3-1 2-.6l4 2c1 .5 1 2 0 3l-1.5 1.5c-1.5 1.5-5 1-9-3s-4.5-7.5-3-9z" fill="#ffffff"/>
        </svg>
        +49 170 5550142
      </li>
      <li class="contact-item">
        <svg class="contact-icon" viewBox="0 0 40 40" aria-hidden="true">
          <rect x="4" y="10" width="32" height="21" fill="none" stroke="var(--icon-cyan)" stroke-width="2.5"/>
          <path d="M4 10l16 12 16-12" fill="none" stroke="var(--icon-cyan)" stroke-width="2.5"/>
        </svg>
        hello@corvanta.com
      </li>
      <li class="contact-item">
        <svg class="contact-icon" viewBox="0 0 40 40" aria-hidden="true">
          <g fill="none" stroke="var(--icon-cyan)" stroke-width="2.5">
            <circle cx="20" cy="20" r="16"/>
            <ellipse cx="20" cy="20" rx="7" ry="16"/>
            <line x1="4" y1="20" x2="36" y2="20"/>
            <path d="M7 12h26M7 28h26"/>
          </g>
        </svg>
        www.corvanta.com
      </li>
    </ul>
  </main>
</body>
</html>
```